Dog Grooming Provisions - Coat Revival Mist *

We are Moss Hollow Meadows. A city dog's country camp. We are a dog services company providing a camp experience in Upstate NY to the dogs of NYC. We are creating a hand made Coat Revival Mist for our clients (who are dogs!) for the holidays.
These labels will be used on a 4 ounce vintage style spray bottles. The design should have a vintage grooming provisions feel. We'd like to see the design be a simple, vintage style black with white, charcoal, or very dark almost black green.
The design should incorporate our varying vintage fonts, our logo with "grooming provisions" all natural & handmade, Coat Revive
Obviously this is a gift and while Coat Revive is important, our brand should be a focus. Perhaps a very simple and "elegant" bone but steer away from paws and pet cheesy! Classic, vintage and camp.

Target Market(s)

Upscale Pet Owners of NYC

Industry/Entity Type

Pet Care

Logo Text

Moss Hollow Meadows Dog Camp (Dog Camp is is for logo not necessary for label)

Font styles to use
Serif
Sans Serif
Script

Colors
9bcb3b
000000
5c5c5c

Requirements
Must have
• I am looking for a black and white or very simple design. I'd even like our logo for this use be black/white (if possible? - not sure if that can happen?)
• Our branding! Simple vintage feel.
• Grooming Provisions
• Coat Revival or Coat Revive or Coat Bright Mist
• Handmade
• All Natural
• Fonts of vintage style - varying with simple and bold (i attached some photos)
Nice to have
• **MAYBE a very Simple Bone (see drawing) - very very thin.
Should not have
• 1. PAWS or cheap looking dog related items
• 2. No bright colors - truly prefer black and white or black with intention to print on plain pulp/brown paper (attached photo)
• 3. Over designed

```html
<!DOCTYPE html>
<html lang="en">
<head>
<meta charset="utf-8">
<title>Coat Revive Spray Label</title>
<link rel="stylesheet" href="https://fonts.googleapis.com/css2?family=Rye&family=Cutive+Mono&family=Allura&family=Bebas+Neue&family=Arimo:wght@400;700&display=swap">
<style>
  :root {
    --ink: #000000;
    --paper: #ffffff;
    --frame: #e1e1e1;
    --badge: #a9b7b7;
    --badge-ink: #2b2b2b;
    --charcoal: #333333;
  }
  * { margin: 0; padding: 0; box-sizing: border-box; }
  html, body { width: 1200px; height: 748px; overflow: hidden; background: var(--paper); }
  .label { position: relative; width: 1200px; height: 748px; background: var(--paper); overflow: hidden; }

  .back-band { position: absolute; left: 593px; top: 178px; width: 607px; height: 570px; background: var(--ink); }

  .front-frame { position: absolute; left: 16px; top: 16px; width: 577px; height: 715px; border: 13px solid var(--frame); background: var(--paper); }
  .front-dark { position: absolute; left: 0; top: 149px; right: 0; bottom: 0; background: var(--ink); }

  .brand-badge {
    position: absolute; left: 204px; top: 69px; width: 192px; height: 192px;
    border-radius: 50%; background: var(--badge); border: 3px solid var(--badge-ink);
    display: flex; align-items: center; justify-content: center; text-align: center;
    font-family: "Cutive Mono", monospace; font-size: 24px; line-height: 1.15; color: var(--badge-ink);
    padding: 0 22px;
  }

  .provisions { position: absolute; left: 0; width: 100%; top: 293px; display: flex; justify-content: center; align-items: center; gap: 8px;
    font-family: "Cutive Mono", monospace; color: var(--paper); }
  .provisions .word { font-size: 15px; letter-spacing: 3px; }
  .provisions .word.small { font-size: 12px; letter-spacing: 2px; }
  .bone { width: 80px; height: 36px; }

  .product-name { position: absolute; left: 0; width: 100%; text-align: center; font-family: "Rye", serif; }
  .front .product-name { top: 402px; font-size: 42px; color: var(--paper); letter-spacing: 1px; }
  .product-type { position: absolute; left: 0; width: 100%; text-align: center; font-family: "Cutive Mono", monospace; letter-spacing: 16px; padding-left: 16px; }
  .front .product-type { top: 469px; font-size: 30px; color: var(--paper); }

  .tagline { position: absolute; left: 0; width: 100%; top: 532px; text-align: center; font-family: "Allura", cursive; font-size: 50px; color: var(--paper); }
  .volume { position: absolute; left: 0; width: 100%; top: 656px; text-align: center; font-family: "Cutive Mono", monospace; font-size: 32px; letter-spacing: 4px; color: var(--paper); }

  .back { position: absolute; left: 593px; top: 0; width: 607px; height: 748px; }
  .back .product-name { top: 55px; font-size: 42px; color: var(--ink); }
  .back .product-type { top: 120px; font-size: 30px; color: var(--charcoal); }

  .info { position: absolute; left: 104px; top: 205px; width: 410px; color: var(--paper); font-family: "Arimo", Arial, sans-serif; }
  .info h2 { font-family: "Bebas Neue", sans-serif; font-weight: 400; font-size: 30px; line-height: 1; display: inline-block; border-bottom: 2px solid var(--paper); margin-bottom: 4px; }
  .info .body-bold { font-weight: 700; font-size: 13.2px; line-height: 1.17; margin-bottom: 14px; }
  .info .body-caps { font-size: 11.2px; line-height: 1.13; text-transform: uppercase; margin-bottom: 12px; }
</style>
</head>
<body>
<main class="label">
  <div class="back-band"></div>

  <section class="front front-frame">
    <div class="front-dark"></div>
    <div class="brand-badge">Moss Hollow Meadows</div>

    <div class="provisions">
      <span class="word">GROOMING</span>
      <svg class="bone" viewBox="0 0 80 36" aria-hidden="true">
        <path fill="#ffffff" d="M10 4 a8 8 0 0 1 12 6 h36 a8 8 0 0 1 12 -6 a8 8 0 0 1 4 14 a8 8 0 0 1 -4 14 a8 8 0 0 1 -12 -6 h-36 a8 8 0 0 1 -12 6 a8 8 0 0 1 -4 -14 a8 8 0 0 1 4 -14 z"/>
      </svg>
      <span class="word small">PROVISIONS</span>
    </div>

    <h1 class="product-name">COAT REVIVE</h1>
    <p class="product-type">SPRAY</p>
    <p class="tagline">Handmade all natural</p>
    <p class="volume">4 ounce</p>
  </section>

  <section class="back">
    <h1 class="product-name">COAT REVIVE</h1>
    <p class="product-type">SPRAY</p>

    <div class="info">
      <h2>How to use</h2>
      <p class="body-bold">Apply twice a day to face and throat all over, or where needed. For best results, thoroughly wash face prior to use.</p>

      <h2>Ingredients</h2>
      <p class="body-bold">Aloe Barbadensis Leaf Juice (Organic Aloe), Aqua (Water), Helianthus Annuus Seed Oil (Organic Sunflower), Isopropyl Palmitate (Plant based), Glyceryl Stearate SE (Plant based), Cetyl Alcohol (Plant based), Stearic Acid (Plant based), Glycerin ( Kosher Vegetable), Butyrospermum Parkii Butter (Organic Shea), Simmondsia Chinesis Seed Oil (Organic Jojoba), Panthenol (Vitamin B5), Tocopherol Acetate (Vitamin E), Camelia Sinensis Leaf Extract (Green Tea), Xanthan Gum (Plant based), Phenoxyethanol (Natural preservative), Ethylhexylglycerin (Plant based)</p>

      <h2>Catuion</h2>
      <p class="body-caps">For external use only. Avoid contact with eyes. If contact occurs, rinse thoroughly with water. Keep out of reach of children.</p>
      <p class="body-caps">This delightful lotion absorbs right into the skin without leaving a greasy feeling yet provides the glide of a deep penetrating moisturizer. It conditions your skin while it moisturizes and softens and will leave your skin glowing.</p>
    </div>
  </section>
</main>
</body>
</html>
```